Dental Office Needs- Flyer Design for Same Day Crowns

We need a flyer that will explain the benefits of the same day crown from the patient prospective. Not show pictures of the machine that makes the crowns. See attached material for content. The flyer should use the practices PMS colors of Green 562 and Blue 3025. The ad should say to the patient - I want to go this office and get my crown done there.
Updates

Project Deadline Extended Reason: The difference in the time zone between USA and Europe has caused issues. Minor changes still need to be worked out. Added Thursday, July 14, 2016

Target Market(s)

Dental Patients

Industry/Entity Type

Dental

Requirements
Must have
• Call to Action
• Business Address and Business Logo
• Classic Design
• images of a Happy 50 year old Couple
• Gives the benefits of the same day crown
Should not have
• No Images of tooth figures
• No before or after pictures

```html
<!DOCTYPE html>
<html lang="en">
<head>
<meta charset="utf-8">
<title>Same-Day Crown Flyer</title>
<link href="https://fonts.googleapis.com/css2?family=Montserrat:wght@600;700;800&family=Arimo:wght@400;700&family=Tinos&display=swap" rel="stylesheet">
<style>
  :root {
    --cream: #eef0dc;
    --green-562: #00705e;
    --green-light: #2f9a86;
    --blue-3025: #004f6e;
    --blue-deep: #003a52;
    --ink: #111111;
    --white: #ffffff;
  }
  * { margin: 0; padding: 0; box-sizing: border-box; }
  html, body { width: 927px; height: 1200px; overflow: hidden; background: var(--white); }
  .flyer {
    position: relative;
    width: 927px;
    height: 1200px;
    background: var(--cream);
    overflow: hidden;
    font-family: "Arimo", Arial, sans-serif;
  }
  .headline {
    position: absolute;
    top: 24px;
    left: 0;
    width: 100%;
    text-align: center;
    font-family: "Montserrat", sans-serif;
    font-weight: 700;
    font-size: 38px;
    line-height: 50px;
    letter-spacing: -0.8px;
    color: var(--blue-3025);
  }
  .hero {
    position: absolute;
    top: 180px;
    left: 0;
    width: 927px;
    height: 455px;
  }
  .goodbyes {
    position: absolute;
    top: 640px;
    left: 0;
    width: 100%;
    text-align: center;
    font-family: "Montserrat", sans-serif;
    font-weight: 700;
    font-size: 27px;
    line-height: 36px;
    color: var(--ink);
  }
  .intro {
    position: absolute;
    top: 776px;
    left: 0;
    width: 100%;
    text-align: center;
    font-weight: 700;
    font-size: 20px;
    line-height: 27px;
    color: var(--ink);
  }
  .benefits-band {
    position: absolute;
    top: 848px;
    left: 0;
    width: 927px;
    height: 200px;
  }
  .benefits {
    position: absolute;
    top: 902px;
    left: 0;
    width: 100%;
    display: flex;
    flex-direction: column;
    align-items: center;
    list-style: none;
    font-size: 25px;
    line-height: 38px;
    color: var(--white);
  }
  .benefit {
    display: flex;
    align-items: center;
    gap: 12px;
    width: 400px;
  }
  .benefit svg { width: 24px; height: 24px; flex: none; }
  .footer {
    position: absolute;
    top: 1048px;
    left: 0;
    width: 927px;
    height: 152px;
    background: var(--white);
  }
  .brand {
    position: absolute;
    left: 40px;
    top: 58px;
    display: flex;
    align-items: center;
    gap: 12px;
    font-family: "Tinos", serif;
    font-size: 30px;
    color: var(--green-562);
  }
  .brand-dot {
    width: 30px;
    height: 30px;
    border-radius: 50%;
    background: var(--green-562);
  }
  .contact {
    position: absolute;
    left: 487px;
    top: 76px;
    font-family: "Tinos", serif;
    font-size: 30px;
    color: var(--ink);
  }
</style>
</head>
<body>
<main class="flyer">
  <h1 class="headline">ARE YOU READY FOR A DRAMATICALLY<br>IMPROVED EXPERIENCE WITH YOUR<br>NEXT CROWN?</h1>

  <svg class="hero" viewBox="0 0 927 455" role="img" aria-label="Photo of a happy couple in their fifties smiling together outdoors in soft green light">
    <defs>
      <linearGradient id="heroFill" x1="0" y1="0" x2="1" y2="0">
        <stop offset="0" stop-color="#86a05a"/>
        <stop offset="0.3" stop-color="#b99a7c"/>
        <stop offset="0.55" stop-color="#d3b198"/>
        <stop offset="0.8" stop-color="#a7b27f"/>
        <stop offset="1" stop-color="#d9e4c4"/>
      </linearGradient>
    </defs>
    <path d="M0 26 Q463 -18 927 26 L927 430 Q463 392 0 455 Z" fill="url(#heroFill)"/>
    <path d="M0 26 Q463 -18 927 26 L927 14 Q463 -30 0 14 Z" fill="var(--green-562)"/>
    <path d="M0 455 Q463 392 927 430 L927 420 Q463 382 0 445 Z" fill="var(--green-562)"/>
  </svg>

  <p class="goodbyes">GOOD-BYE TEMPORARY CROWN<br>GOOD-BYE SECOND APPOINTMENT<br>GOOD-BYE GOOEY MESSY IMPRESSIONS</p>

  <p class="intro">Brookfield Dental Care is pleased to offer you the Comfort and<br>Convenience of One Visit Dental Care.</p>

  <svg class="benefits-band" viewBox="0 0 927 200" preserveAspectRatio="none" aria-hidden="true">
    <defs>
      <linearGradient id="bandFill" x1="0" y1="0" x2="1" y2="1">
        <stop offset="0" stop-color="var(--green-light)"/>
        <stop offset="0.45" stop-color="var(--green-562)"/>
        <stop offset="1" stop-color="var(--blue-3025)"/>
      </linearGradient>
    </defs>
    <path d="M0 22 Q300 -10 927 26 L927 200 L0 200 Z" fill="var(--blue-3025)" opacity="0.35"/>
    <path d="M0 30 Q300 2 927 34 L927 200 L0 200 Z" fill="url(#bandFill)"/>
  </svg>

  <ul class="benefits">
    <li class="benefit"><svg viewBox="0 0 24 24" aria-hidden="true"><path d="M4 12 L10 18 L20 6" fill="none" stroke="#ffffff" stroke-width="3" stroke-linecap="round" stroke-linejoin="round"/></svg>A Same-Day Restoration</li>
    <li class="benefit"><svg viewBox="0 0 24 24" aria-hidden="true"><path d="M4 12 L10 18 L20 6" fill="none" stroke="#ffffff" stroke-width="3" stroke-linecap="round" stroke-linejoin="round"/></svg>A Stronger More Precise Fit</li>
    <li class="benefit"><svg viewBox="0 0 24 24" aria-hidden="true"><path d="M4 12 L10 18 L20 6" fill="none" stroke="#ffffff" stroke-width="3" stroke-linecap="round" stroke-linejoin="round"/></svg>A Beautiful Natural Appearance</li>
  </ul>

  <footer class="footer">
    <div class="brand"><span class="brand-dot"></span>Brookfield Dental Care</div>
    <p class="contact">contact info here</p>
  </footer>
</main>
</body>
</html>
```